RUV Coffee bag (front and back)

We use black matte bags and have front and back labels. We have a logo but need an attractive and inviting label. The labels will be used for our entire line of coffees. We sell most of our coffee to foodservice establishments (Restaurants, Hotels, Bakeries, Bodegas) and we would like to have these establishments display our bags of coffee to sell retail.
The logo can be used as a whole or using any one of the three components (Logo, image, tag).

Target Market(s)

People who buy the coffee they brew at home from the local shop they get their morning latte.. We are a local coffee company, but we do not sell locally roasted coffee!

Industry/Entity Type

Food

Font styles to use
Other font styles liked:
• something that looks good with our trademarked RUV

Colors

Designer to choose colors to be used in the design.

Requirements
Must have
• Respect Trademarked logo
Nice to have
• It would be nice to have a design that can be used with other mediums (airpot wraps, java jackets, )
Should not have
• Real People

```html
<!DOCTYPE html>
<html lang="en">
<head>
<meta charset="utf-8">
<title>RUV Coffee – Bold Crema Espresso bag front</title>
<link rel="stylesheet" href="https://fonts.googleapis.com/css2?family=Josefin+Sans:wght@300;400;600&display=swap">
<style>
  :root {
    --surface: #f4f4f4;
    --bag-black: #1c1c1c;
    --bag-shade: #262626;
    --ink-white: #f5f5f5;
    --accent-red: #d42a2a;
    --rule-grey: #bdbdbd;
  }
  * { margin: 0; padding: 0; box-sizing: border-box; }
  html, body {
    width: 1200px;
    height: 962px;
    overflow: hidden;
    background: var(--surface);
    font-family: "Josefin Sans", sans-serif;
  }
  .canvas {
    position: relative;
    width: 1200px;
    height: 962px;
  }
  .bag-front {
    position: absolute;
    left: 340px;
    top: 40px;
    width: 520px;
    height: 882px;
    background: var(--bag-black);
    overflow: hidden;
  }
  .bag-pattern {
    position: absolute;
    inset: 0;
    background: radial-gradient(ellipse at 50% 30%, var(--bag-shade) 0%, var(--bag-black) 75%);
  }
  .seal-line {
    position: absolute;
    left: 0;
    right: 0;
    height: 2px;
    background: #2e2e2e;
  }
  .seal-line.top { top: 54px; }
  .seal-line.zip { top: 92px; }
  .brand {
    position: absolute;
    top: 150px;
    left: 0;
    right: 0;
    display: flex;
    flex-direction: column;
    align-items: center;
  }
  .brand-mark {
    display: flex;
    align-items: center;
    gap: 18px;
  }
  .brand-dot {
    width: 34px;
    height: 34px;
    border: 4px solid var(--accent-red);
    border-radius: 50%;
  }
  .brand-name {
    color: var(--ink-white);
    font-weight: 300;
    font-size: 92px;
    letter-spacing: 6px;
    line-height: 1;
  }
  .brand-tag {
    margin-top: 8px;
    color: var(--ink-white);
    font-weight: 300;
    font-size: 11px;
    letter-spacing: 3px;
  }
  .product {
    position: absolute;
    left: 100px;
    top: 430px;
    width: 340px;
  }
  .product-name {
    color: var(--ink-white);
    font-weight: 300;
    font-size: 50px;
    line-height: 1.0;
    letter-spacing: 1px;
    text-transform: uppercase;
  }
  .product-rule {
    margin-top: 14px;
    height: 1px;
    background: var(--rule-grey);
  }
  .product-desc {
    margin-top: 8px;
    color: var(--accent-red);
    font-weight: 300;
    font-size: 18px;
    letter-spacing: 0.5px;
    text-transform: uppercase;
  }
  .product-rule.lower { margin-top: 8px; }
  .specs {
    margin-top: 16px;
    display: flex;
    align-items: center;
    gap: 12px;
    color: var(--ink-white);
    text-transform: uppercase;
  }
  .spec-dot {
    width: 18px;
    height: 18px;
    border-radius: 50%;
    background: var(--ink-white);
  }
  .spec-roast {
    font-size: 15px;
    font-weight: 400;
    line-height: 1.05;
  }
  .spec-divider {
    width: 1px;
    height: 34px;
    background: var(--ink-white);
  }
  .spec-weight {
    display: flex;
    align-items: flex-end;
    font-weight: 600;
  }
  .spec-weight .num { font-size: 36px; line-height: 0.9; }
  .spec-weight .unit { font-size: 14px; margin-left: 2px; }
  .spec-form {
    font-size: 13px;
    font-weight: 400;
    line-height: 1.0;
  }
</style>
</head>
<body>
<main class="canvas">
  <section class="bag-front">
    <div class="bag-pattern" role="img" aria-label="Subtle tone-on-tone repeating swirl pattern across the black matte bag"></div>
    <div class="seal-line top"></div>
    <div class="seal-line zip"></div>

    <header class="brand">
      <div class="brand-mark">
        <span class="brand-dot"></span>
        <span class="brand-name">RUV</span>
      </div>
      <span class="brand-tag">Riverside Urban Varietals</span>
    </header>

    <div class="product">
      <h1 class="product-name">Bold<br>Crema<br>Espresso</h1>
      <div class="product-rule"></div>
      <p class="product-desc">A rich, classic espresso blend</p>
      <div class="product-rule lower"></div>
      <div class="specs">
        <span class="spec-dot"></span>
        <span class="spec-roast">Espresso<br>Roast</span>
        <span class="spec-divider"></span>
        <span class="spec-weight"><span class="num">2</span><span class="unit">LB</span></span>
        <span class="spec-form">Whole<br>Bean<br>Coffee</span>
      </div>
    </div>
  </section>
</main>
</body>
</html>
```